Broschüre im Bereich Steuerberatung
Zielgruppe
Steuerberatung
Aufgabenstellung
Die Seite 1 wäre eigentlich fertig, natürlich bin ich offen für Optimierungen. Die weiteren fünf Seiten gilt es noch zu gestalten:
Seite 1
Buchhaltung
Lohnwesen
Steuern
Firmengründung
Kontakt

```html
<!DOCTYPE html>
<html lang="de">
<head>
<meta charset="utf-8">
<title>Morlen Treuhand – Kontakt</title>
<link href="https://fonts.googleapis.com/css2?family=Nunito:wght@900&family=Jost:wght@400&display=swap" rel="stylesheet">
<style>
  :root {
    --navy: #0d3a7c;
    --orange: #e8600f;
    --link: #1b5c8c;
    --ink: #1a1a1a;
    --map-tint: #eef0f6;
    --paper: #ffffff;
  }
  html, body { margin: 0; padding: 0; overflow: hidden; }
  body { width: 1200px; height: 849px; background: var(--paper); position: relative; font-family: "Jost", sans-serif; }
  .intro { position: absolute; left: 52px; top: 164px; }
  .intro__title { margin: 0; font-family: "Nunito", sans-serif; font-weight: 900; color: var(--navy); font-size: 18.5px; line-height: 24px; }
  .intro__lead { margin: 8px 0 0; font-family: "Nunito", sans-serif; font-weight: 900; color: var(--orange); font-size: 14.5px; line-height: 19.5px; }
  .office { position: absolute; top: 396px; width: 540px; height: 346px; }
  .office--luzern { left: 50px; }
  .office--uferdorf { left: 626px; }
  .brand { position: absolute; left: 0; top: 50px; display: flex; align-items: center; gap: 10px; }
  .brand__dot { width: 22px; height: 22px; border-radius: 50%; background: var(--orange); }
  .brand__name { font-family: "Jost", sans-serif; font-weight: 400; font-size: 56px; color: var(--navy); letter-spacing: 1px; line-height: 1; }
  .address { position: absolute; left: 35px; top: 184px; margin: 0; font-style: normal; font-size: 13.5px; line-height: 20.2px; color: var(--ink); }
  .address a { color: var(--link); text-decoration: none; }
  .map { position: absolute; left: 215px; top: 0; width: 293px; height: 346px; }
  .divider { position: absolute; left: 599px; top: 396px; width: 1px; height: 346px; background: var(--navy); }
</style>
</head>
<body>
  <header class="intro">
    <h1 class="intro__title">Zuverlässig und partnerschaftlich:<br>Ihre massgeschneiderten Treuhand-Lösungen</h1>
    <p class="intro__lead">Sie haben noch Fragen? Rufen Sie uns an oder senden<br>Sie uns eine Mail, wir helfen Ihnen gerne weiter.</p>
  </header>

  <section class="office office--luzern">
    <div class="brand"><span class="brand__dot"></span><span class="brand__name">morlen</span></div>
    <address class="address">
      Morlen Treuhand<br>Consulting GmbH<br>Talackerweg 12<br>6099 Seeblick<br>
      Telefon +41 (0) 44 555 18 40<br>Mobile +41 (0)79 555 30 70<br>
      info@morlentreuhand.ch<br><a href="#">www.morlentreuhand.ch</a>
    </address>
    <svg class="map" role="img" aria-label="Lageplan des Büros Seeblick mit Strassen und Standortmarkierung" viewBox="0 0 293 346">
      <rect width="293" height="346" fill="var(--map-tint)"/>
    </svg>
  </section>

  <div class="divider"></div>

  <section class="office office--uferdorf">
    <div class="brand"><span class="brand__dot"></span><span class="brand__name">morlen</span></div>
    <address class="address">
      Morlen Treuhand<br>Consulting GmbH<br>Föhrenrain 8<br>8899 Uferdorf<br>
      Telefon +41 (0) 44 555 18 40<br>Mobile +41 (0)79 555 30 70<br>
      info@morlentreuhand.ch<br><a href="#">www.morlentreuhand.ch</a>
    </address>
    <svg class="map" role="img" aria-label="Lageplan des Büros Uferdorf mit Strassen und Standortmarkierung" viewBox="0 0 293 346">
      <rect width="293" height="346" fill="var(--map-tint)"/>
    </svg>
  </section>
</body>
</html>
```